Paint Protection Options

This is a flyer that will describe two different paint protection options for vehicles. I have mocked up a Word doc. As well, I've included some samples of other flyers where I like the "look". I am not locked into any single layout or design. In my Word doc I have them side-by-side. I think that makes sense but open to ideas. I've also added some pics of the two options being applied to cars. We need to have one of each (ceramic and ppf) at a minimum. In the grid I'm thinking different colors dots/circles to differentiate the different levels. But again, I'm open to suggestions. You can use the symbol for microns in the grid under the Thickness row. I spelled it out because I didn't know how to insert.

```html
<!DOCTYPE html>
<html lang="en">
<head>
<meta charset="utf-8">
<title>Paint Protection Options</title>
<link rel="stylesheet" href="https://fonts.googleapis.com/css2?family=Poppins:wght@300;400;500;600;700;800;900&family=Montserrat:wght@800&display=swap">
<style>
:root{
  --stage:#a6a6a6;
  --charcoal:#1f2021;
  --charcoal-2:#3a3b3c;
  --green:#3db54a;
  --green-dark:#1f7a34;
  --cyan:#33c3e6;
  --gold:#d2a02c;
  --card:#f2f2f2;
  --ink:#2b2b2b;
  --muted:#555;
  --blue:#2f64bd;
  --pink:#e3205a;
  --tick-blue:#3a6fd0;
  --tick-green:#3db54a;
  --tick-yellow:#d9c21f;
  --tick-red:#d9262b;
  --rule:#c9c9c9;
}
*{box-sizing:border-box;margin:0;padding:0}
html,body{width:1200px;height:1200px;overflow:hidden;background:var(--stage);font-family:"Poppins",sans-serif}
.flyer{position:absolute;left:180px;top:6px;width:840px;height:1188px;
  background:radial-gradient(ellipse at 30% 40%,var(--charcoal-2),var(--charcoal) 70%);overflow:hidden}
.title-banner{position:absolute;left:48px;top:46px;width:750px;height:70px;border-radius:18px 18px 0 0;
  background:linear-gradient(90deg,var(--green),#2f9a3f 60%,var(--green-dark));
  display:flex;align-items:center;justify-content:center}
.title-banner h1{color:#fff;font-weight:900;font-size:43px;letter-spacing:-0.5px;line-height:1}
.title-banner::after{content:"";position:absolute;left:367px;bottom:-8px;border:8px solid transparent;border-top-color:#2f9a3f;border-bottom:0}
.photo{position:absolute;top:133px;height:139px}
.photo-ceramic{left:48px;width:368px;background:linear-gradient(135deg,#d9dde6,#2a3f9a 45%,#e07a3a 55%,#1b2a6e)}
.photo-ppf{left:419px;width:379px;background:linear-gradient(135deg,#b3202c,#8a1820 40%,#9aa0a8 65%,#2a2c30)}
.info-card{position:absolute;left:48px;top:277px;width:750px;height:444px;background:var(--card);border-radius:0 0 12px 12px;overflow:hidden}
.side-label{position:absolute;top:0;height:100%;display:flex;align-items:center;justify-content:center}
.side-label span{transform:rotate(-90deg);white-space:nowrap;color:#fff;font-family:"Montserrat",sans-serif;font-weight:800}
.side-ceramic{left:0;width:43px;background:var(--cyan)}
.side-ceramic span{font-size:24px}
.side-ppf{right:0;width:47px;background:var(--gold)}
.side-ppf span{font-size:22px}
.divider{position:absolute;left:370px;top:4px;bottom:8px;border-left:1px dashed #888}
.copy{position:absolute;top:13px;color:var(--muted);font-size:14.2px;font-weight:300;line-height:16.7px;letter-spacing:-0.15px}
.copy p{margin-bottom:16.7px}
.copy-ceramic{left:68px;width:290px}
.copy-ppf{left:395px;width:292px}
.benefits{list-style:none}
.benefits li{position:relative;padding-left:23px;font-weight:600;color:var(--ink);font-size:14.2px;line-height:16.7px;margin-bottom:5px}
.copy-ppf .benefits li{margin-bottom:9px}
.benefits svg{position:absolute;left:0;top:0}
.compare{position:absolute;left:49px;top:753px;width:755px}
.compare-head{display:grid;grid-template-columns:239px 171px 172px 173px;height:45px;align-items:end}
.compare-head div{height:45px;display:flex;align-items:center;padding-left:22px;color:#fff;font-weight:600;font-size:15px;border-radius:10px 10px 0 0;border-top:3px solid rgba(255,255,255,.35)}
.compare-head .feature-title{height:33px;border-radius:0;border:0;background:#c8c8c8;color:var(--ink);font-weight:700;font-size:21px;padding-left:31px}
.compare-head .head-wax{background:linear-gradient(160deg,#3d73d0,var(--blue))}
.compare-head .head-ceramic{background:linear-gradient(160deg,#ef3b6c,var(--pink));padding-left:18px}
.compare-head .head-ppf{background:linear-gradient(160deg,#4fca58,var(--green));padding-left:12px}
.compare-body{display:grid;grid-template-columns:239px 171px 172px 173px;grid-auto-rows:27.4px;background:#fff}
.feature{display:flex;align-items:center;gap:6px;padding-left:14px;font-size:15px;color:var(--ink);background:#fff}
.feature svg{flex:none}
.cell{display:flex;align-items:center;gap:6px;padding-left:12px;font-size:13.6px;color:var(--ink);background:var(--card);border-bottom:1px solid var(--rule);border-left:2px solid #fff}
.dot{width:11px;height:11px;flex:none}
.compare-foot{display:grid;grid-template-columns:239px 171px 172px 173px;height:32px}
.compare-foot div{display:flex;align-items:center;color:#fff;font-weight:600;font-size:14px}
.compare-foot .foot-label{background:#c8c8c8;color:var(--ink);font-size:15.5px;padding-left:20px}
.foot-wax{background:var(--blue);padding-left:31px}
.foot-ceramic{background:var(--pink);padding-left:32px}
.foot-ppf{background:var(--green);padding-left:29px}
</style>
</head>
<body>
<svg width="0" height="0" style="position:absolute">
  <defs>
    <symbol id="diamond-tick" viewBox="0 0 16 16"><path d="M8 1 15 8 8 15 1 8Z" fill="none" stroke="#3db54a" stroke-width="1.4"/><path d="M5 8.2 7.2 10.3 11 6" fill="none" stroke="#3db54a" stroke-width="1.4"/></symbol>
    <symbol id="tick" viewBox="0 0 12 12"><path d="M3.3 6.2 5.2 8 8.8 4.3" fill="none" stroke="#fff" stroke-width="1.5"/></symbol>
    <symbol id="feature-icon" viewBox="0 0 18 18"><circle cx="9" cy="9" r="6.5" fill="none" stroke="#3a6fd0" stroke-width="1.2"/><path d="M6 9h6M9 6v6" stroke="#3a6fd0" stroke-width="1"/></symbol>
  </defs>
</svg>

<main class="flyer">
  <header class="title-banner"><h1>PAINT PROTECTION OPTIONS</h1></header>

  <div class="photo photo-ceramic" role="img" aria-label="Photo of a cloth buffing ceramic coating onto a blue car"></div>
  <div class="photo photo-ppf" role="img" aria-label="Photo of hands applying clear protection film to a red car"></div>

  <section class="info-card">
    <div class="side-label side-ceramic"><span>CERAMIC COATINGS</span></div>
    <div class="divider"></div>
    <div class="copy copy-ceramic">
      <p>Ceramic coatings are liquid polymer coatings that bond to a vehicle’s painted surface. The coatings are formulated to retain the showroom finish by protecting against corrosion and contaminants like UV damage, oxidation, road salt and acid rain. Ceramic coatings give your car a deep, glossy finish that reflects light and makes your paint look more vibrant while greatly extending the paint's lifespan.</p>
      <p>The chemical bonding process improves color depth and leaves a smooth finish. The hydrophobic (water repellent) properties repel water and dirt as well as protect against damaging pollutants. This makes care and maintenance a breeze while retaining the show room finish. Never wax again!</p>
      <ul class="benefits">
        <li><svg width="16" height="16"><use href="#diamond-tick"/></svg>Enhance and retain showroom finish</li>
        <li><svg width="16" height="16"><use href="#diamond-tick"/></svg>Protect against corrosion and contaminants</li>
        <li><svg width="16" height="16"><use href="#diamond-tick"/></svg>Reduce care and maintenance</li>
      </ul>
    </div>
    <div class="copy copy-ppf">
      <p>Paint Protection Film (PPF) is a transparent, thermoplastic urethane film that is applied directly to the car’s painted surfaces. PPF excels at shielding your vehicle from rock chips, scratches, and other physical damage. It has self-healing properties that can repair minor scratches and swirl marks over time.</p>
      <p>Every piece of PPF is custom cut to fit each panel of your vehicle and provide maximum coverage. The film protects your vehicle from scratches, rock chips, staining, corrosion, fading, chemicals, insects, and road debris. It helps keep your paint looking new, saving you money and improving your resale value.</p>
      <ul class="benefits">
        <li><svg width="16" height="16"><use href="#diamond-tick"/></svg>Protect against rock chips, scratches, and physical damage</li>
        <li><svg width="16" height="16"><use href="#diamond-tick"/></svg>Easily repair minor scratches and swirl marks</li>
        <li><svg width="16" height="16"><use href="#diamond-tick"/></svg>Protect against corrosion and contaminants</li>
      </ul>
    </div>
    <div class="side-label side-ppf"><span>PAINT PROTECTION FILM (PPF)</span></div>
  </section>

  <section class="compare">
    <div class="compare-head">
      <div class="feature-title">FEATURE</div>
      <div class="head-wax">Car Wax</div>
      <div class="head-ceramic">Ceramic Coating</div>
      <div class="head-ppf">Paint Protection Film</div>
    </div>
    <div class="compare-body">
      <div class="feature"><svg width="18" height="18"><use href="#feature-icon"/></svg>Duration</div>
      <div class="cell"><svg class="dot"><circle cx="5.5" cy="5.5" r="5.5" fill="var(--tick-blue)"/><use href="#tick" width="11" height="11"/></svg>2 - 4 Weeks</div>
      <div class="cell"><svg class="dot"><circle cx="5.5" cy="5.5" r="5.5" fill="var(--tick-blue)"/><use href="#tick" width="11" height="11"/></svg>3 - 10 Years</div>
      <div class="cell"><svg class="dot"><circle cx="5.5" cy="5.5" r="5.5" fill="var(--tick-blue)"/><use href="#tick" width="11" height="11"/></svg>7 - 10 Years</div>

      <div class="feature"><svg width="18" height="18"><use href="#feature-icon"/></svg>Thickness</div>
      <div class="cell"><svg class="dot"><circle cx="5.5" cy="5.5" r="5.5" fill="var(--tick-blue)"/><use href="#tick" width="11" height="11"/></svg>.5 - 1.5 microns</div>
      <div class="cell"><svg class="dot"><circle cx="5.5" cy="5.5" r="5.5" fill="var(--tick-blue)"/><use href="#tick" width="11" height="11"/></svg>7 - 10 microns</div>
      <div class="cell"><svg class="dot"><circle cx="5.5" cy="5.5" r="5.5" fill="var(--tick-blue)"/><use href="#tick" width="11" height="11"/></svg>200 - 250 microns</div>

      <div class="feature"><svg width="18" height="18"><use href="#feature-icon"/></svg>Gloss Enhancement</div>
      <div class="cell"><svg class="dot"><circle cx="5.5" cy="5.5" r="5.5" fill="var(--tick-green)"/><use href="#tick" width="11" height="11"/></svg>Full Circle - green</div>
      <div class="cell"><svg class="dot"><circle cx="5.5" cy="5.5" r="5.5" fill="var(--tick-green)"/><use href="#tick" width="11" height="11"/></svg>Full Circle - green</div>
      <div class="cell"><svg class="dot"><circle cx="5.5" cy="5.5" r="5.5" fill="var(--tick-green)"/><use href="#tick" width="11" height="11"/></svg>Full Circle - green</div>

      <div class="feature"><svg width="18" height="18"><use href="#feature-icon"/></svg>Acid Rain Damage</div>
      <div class="cell"><svg class="dot"><circle cx="5.5" cy="5.5" r="5.5" fill="var(--tick-yellow)"/><use href="#tick" width="11" height="11"/></svg>1/2 Circle - Yellow</div>
      <div class="cell"><svg class="dot"><circle cx="5.5" cy="5.5" r="5.5" fill="var(--tick-green)"/><use href="#tick" width="11" height="11"/></svg>Full Circle - green</div>
      <div class="cell"><svg class="dot"><circle cx="5.5" cy="5.5" r="5.5" fill="var(--tick-green)"/><use href="#tick" width="11" height="11"/></svg>Full Circle - green</div>

      <div class="feature"><svg width="18" height="18"><use href="#feature-icon"/></svg>Corrosion Prevention</div>
      <div class="cell"><svg class="dot"><circle cx="5.5" cy="5.5" r="5.5" fill="var(--tick-yellow)"/><use href="#tick" width="11" height="11"/></svg>1/2 Circle - Yellow</div>
      <div class="cell"><svg class="dot"><circle cx="5.5" cy="5.5" r="5.5" fill="var(--tick-green)"/><use href="#tick" width="11" height="11"/></svg>Full Circle - green</div>
      <div class="cell"><svg class="dot"><circle cx="5.5" cy="5.5" r="5.5" fill="var(--tick-green)"/><use href="#tick" width="11" height="11"/></svg>Full Circle - green</div>

      <div class="feature"><svg width="18" height="18"><use href="#feature-icon"/></svg>UV/Oxidation Protection</div>
      <div class="cell"><svg class="dot"><circle cx="5.5" cy="5.5" r="5.5" fill="var(--tick-yellow)"/><use href="#tick" width="11" height="11"/></svg>1/2 Circle - Yellow</div>
      <div class="cell"><svg class="dot"><circle cx="5.5" cy="5.5" r="5.5" fill="var(--tick-green)"/><use href="#tick" width="11" height="11"/></svg>Full Circle - green</div>
      <div class="cell"><svg class="dot"><circle cx="5.5" cy="5.5" r="5.5" fill="var(--tick-green)"/><use href="#tick" width="11" height="11"/></svg>Full Circle - green</div>

      <div class="feature"><svg width="18" height="18"><use href="#feature-icon"/></svg>Hard Water Damage</div>
      <div class="cell"><svg class="dot"><circle cx="5.5" cy="5.5" r="5.5" fill="var(--tick-yellow)"/><use href="#tick" width="11" height="11"/></svg>1/4 Circle - Yellow</div>
      <div class="cell"><svg class="dot"><circle cx="5.5" cy="5.5" r="5.5" fill="var(--tick-blue)"/><use href="#tick" width="11" height="11"/></svg>3/4 Circle - green</div>
      <div class="cell"><svg class="dot"><circle cx="5.5" cy="5.5" r="5.5" fill="var(--tick-green)"/><use href="#tick" width="11" height="11"/></svg>Full Circle - green</div>

      <div class="feature"><svg width="18" height="18"><use href="#feature-icon"/></svg>Insect Splatter Damage</div>
      <div class="cell"><svg class="dot"><circle cx="5.5" cy="5.5" r="5.5" fill="var(--tick-yellow)"/><use href="#tick" width="11" height="11"/></svg>1/4 Circle - Yellow</div>
      <div class="cell"><svg class="dot"><circle cx="5.5" cy="5.5" r="5.5" fill="var(--tick-blue)"/><use href="#tick" width="11" height="11"/></svg>3/4 Circle - green</div>
      <div class="cell"><svg class="dot"><circle cx="5.5" cy="5.5" r="5.5" fill="var(--tick-green)"/><use href="#tick" width="11" height="11"/></svg>Full Circle - green</div>

      <div class="feature"><svg width="18" height="18"><use href="#feature-icon"/></svg>Chip Protection</div>
      <div class="cell"><svg class="dot"><circle cx="5.5" cy="5.5" r="5.5" fill="var(--tick-red)"/><use href="#tick" width="11" height="11"/></svg>Full Circle -red</div>
      <div class="cell"><svg class="dot"><circle cx="5.5" cy="5.5" r="5.5" fill="var(--tick-yellow)"/><use href="#tick" width="11" height="11"/></svg>1/4 Circle - Yellow</div>
      <div class="cell"><svg class="dot"><circle cx="5.5" cy="5.5" r="5.5" fill="var(--tick-green)"/><use href="#tick" width="11" height="11"/></svg>Full Circle - green</div>

      <div class="feature"><svg width="18" height="18"><use href="#feature-icon"/></svg>Scratch Protection</div>
      <div class="cell"><svg class="dot"><circle cx="5.5" cy="5.5" r="5.5" fill="var(--tick-red)"/><use href="#tick" width="11" height="11"/></svg>Full Circle -red</div>
      <div class="cell"><svg class="dot"><circle cx="5.5" cy="5.5" r="5.5" fill="var(--tick-yellow)"/><use href="#tick" width="11" height="11"/></svg>1/4 Circle - Yellow</div>
      <div class="cell"><svg class="dot"><circle cx="5.5" cy="5.5" r="5.5" fill="var(--tick-green)"/><use href="#tick" width="11" height="11"/></svg>Full Circle - green</div>

      <div class="feature"><svg width="18" height="18"><use href="#feature-icon"/></svg>Swirl Protection</div>
      <div class="cell"><svg class="dot"><circle cx="5.5" cy="5.5" r="5.5" fill="var(--tick-red)"/><use href="#tick" width="11" height="11"/></svg>Full Circle -red</div>
      <div class="cell"><svg class="dot"><circle cx="5.5" cy="5.5" r="5.5" fill="var(--tick-red)"/><use href="#tick" width="11" height="11"/></svg>Full Circle -red</div>
      <div class="cell"><svg class="dot"><circle cx="5.5" cy="5.5" r="5.5" fill="var(--tick-green)"/><use href="#tick" width="11" height="11"/></svg>Full Circle - green</div>
    </div>
    <div class="compare-foot">
      <div class="foot-label">Application Complexity</div>
      <div class="foot-wax">Low</div>
      <div class="foot-ceramic">Medium</div>
      <div class="foot-ppf">High</div>
    </div>
  </section>
</main>
</body>
</html>
```